Maple Hollow Canine Massage Needs a Business Card Design

Maple Hollow Canine Massage is a new therapeutic canine massage company located in Nederland, Colorado. I need a business card design that include my logo and basic contact information.

Target Market(s)

Pet owners, veterinarians

Industry/Entity Type

Business

Contact Information for Business Card

Lydia Ferrow, CCMT
303.518.7269
lydia@maplehollowmassage.example
www.maplehollowmassage.example

Colors
6c459b
886aae
b8a6cd
a64599
b768aa
d3a5cc
fbed22

Requirements
Must have
• Font should be similar to font in logo.

```html
<!DOCTYPE html>
<html lang="en">
<head>
<meta charset="utf-8">
<title>Maple Hollow Canine Massage – Business Card</title>
<link rel="stylesheet" href="https://fonts.googleapis.com/css2?family=PT+Sans:wght@400;700&display=swap">
<style>
  :root {
    --backdrop: #c4c7ca;
    --card: #ffffff;
    --violet-deep: #6c459b;
    --lavender: #b8a6cd;
    --lavender-mid: #886aae;
    --orchid: #a64599;
    --orchid-soft: #b768aa;
    --gold: #e2b430;
  }
  * { margin: 0; padding: 0; box-sizing: border-box; }
  html, body {
    width: 1200px; height: 900px; overflow: hidden;
    background: var(--backdrop);
    font-family: "PT Sans", "Myriad Pro", sans-serif;
  }
  .canvas {
    width: 1200px; height: 900px;
    display: flex; align-items: center; justify-content: center;
  }
  .business-card {
    position: relative;
    width: 440px; height: 770px;
    background: var(--card);
    box-shadow: 0 10px 30px rgba(0,0,0,0.18);
    overflow: hidden;
    text-align: center;
  }
  .logo-block {
    position: absolute; top: 42px; left: 0; right: 0;
    display: flex; flex-direction: column; align-items: center;
  }
  .logo-disc {
    width: 250px; height: 250px; border-radius: 50%;
    background: var(--lavender-mid);
    border: 5px solid var(--gold);
    display: flex; align-items: center; justify-content: center;
  }
  .logo-name {
    font-weight: 700; font-size: 30px; line-height: 1.15;
    color: var(--card);
    width: 190px;
  }
  .company-name {
    position: absolute; top: 372px; left: 0; right: 0;
    font-size: 29px; font-weight: 400; color: var(--orchid);
  }
  .person-name {
    position: absolute; top: 452px; left: 0; right: 0;
    font-size: 27px; color: var(--orchid);
  }
  .contact-list {
    position: absolute; top: 512px; left: 0; right: 0;
    list-style: none;
    font-size: 19px; line-height: 1.32; color: var(--orchid-soft);
  }
  .card-band {
    position: absolute; left: 0; bottom: 0;
    width: 440px; height: 90px;
  }
</style>
</head>
<body>
<main class="canvas">
  <article class="business-card">
    <div class="logo-block">
      <div class="logo-disc">
        <span class="logo-name">Maple Hollow Canine Massage</span>
      </div>
    </div>

    <h1 class="company-name">Maple Hollow Canine Massage</h1>
    <h2 class="person-name">Lydia Ferrow, CCMT</h2>
    <ul class="contact-list">
      <li>303.518.7269</li>
      <li>lydia@maplehollowmassage.example</li>
      <li>www.maplehollowmassage.example</li>
    </ul>

    <svg class="card-band" viewBox="0 0 440 90" aria-hidden="true">
      <path d="M0 74 H100 V56 Q100 36 120 36 H400 Q416 36 420 48 L424 56 H440 V90 H0 Z"
            fill="var(--lavender)"/>
    </svg>
  </article>
</main>
</body>
</html>
```